The most modern business card ever !!!

Our company call “Vantilo”. Vantilo is a technology company specialized in cruises solutions. Out main product is a platform to reserve cruises. This is a revolutionary platform that make easier to travel agencies and final users to reserve cruises across dozen companies like tarvik, welbi, dpv, hbt, etc..We are a “start up”, with a young team of developers and we want to transmit it.. For it, we want something different, a modern business card that represent cruises and technology.. When someone receive this card, this person should say: wowww this is different… this is modern… this is a cruise related company..
Contact Information for Business Card
Requirements
Must have
- diferent, modern
Should not have
- traditions business card

```html
<!DOCTYPE html>
<html lang="en">
<head>
<meta charset="utf-8">
<title>Vantilo Business Card</title>
<link rel="stylesheet" href="https://fonts.googleapis.com/css2?family=Montserrat:wght@400;500;600;700;800&display=swap">
<style>
  :root {
    --backdrop: #f4f4f4;
    --paper: #ffffff;
    --ink: #000000;
    --sky: #29a8e0;
    --sky-deep: #1b86b8;
    --sea-line: #29a8e0;
    --photo-light: #c9d3dc;
    --photo-dark: #6b5a4c;
  }
  html, body {
    margin: 0;
    padding: 0;
    width: 1185px;
    height: 1200px;
    overflow: hidden;
    background: var(--backdrop);
  }
  .canvas {
    position: relative;
    width: 1185px;
    height: 1200px;
    font-family: "Montserrat", sans-serif;
  }
  .card {
    position: absolute;
    left: 260px;
    width: 664px;
    height: 380px;
    background: var(--paper);
    overflow: hidden;
  }
  .card svg { display: block; width: 100%; height: 100%; }
  .card-front { top: 153px; }
  .card-back { top: 671px; }
  .band { fill: var(--sky); }
  .band-fold { fill: var(--sky-deep); }
  .bar { fill: var(--ink); }
  .wave-line { fill: none; stroke: var(--sea-line); stroke-width: 1.2; stroke-linecap: round; opacity: 0.55; }
  .wave-line.faint { opacity: 0.3; }
  .brand-name { font-family: "Montserrat", sans-serif; font-weight: 600; font-size: 50px; fill: var(--ink); letter-spacing: 0.5px; }
  .brand-web { font-family: "Montserrat", sans-serif; font-weight: 700; font-size: 16.5px; fill: var(--ink); letter-spacing: 0.8px; }
  .brand-web .accent { fill: var(--sky); }
  .person-name { font-family: "Montserrat", sans-serif; font-weight: 700; font-size: 21px; fill: var(--ink); }
  .person-role { font-family: "Montserrat", sans-serif; font-weight: 500; font-size: 12.5px; fill: var(--sky); letter-spacing: 0.4px; }
  .contact-text { font-family: "Montserrat", sans-serif; font-weight: 500; font-size: 12px; fill: var(--paper); letter-spacing: 0.3px; }
  .icon-disc { fill: var(--sky); }
  .icon-line { fill: none; stroke: var(--ink); stroke-width: 1.6; stroke-linejoin: round; stroke-linecap: round; }
  .icon-fill { fill: var(--ink); }
</style>
</head>
<body>
<main class="canvas">

  <section class="card card-front" aria-label="Card front">
    <svg viewBox="0 0 498 285" preserveAspectRatio="none">
      <rect class="bar" x="0" y="223" width="498" height="37"/>
      <g class="sea-waves">
        <path class="wave-line" d="M6,236 q10,-6 20,0 t20,0 t20,0 t20,0 t20,0 t20,0 t20,0 t20,0"/>
        <path class="wave-line faint" d="M16,247 q10,-6 20,0 t20,0 t20,0 t20,0 t20,0 t20,0 t20,0"/>
        <path class="wave-line" d="M332,236 q10,-6 20,0 t20,0 t20,0 t20,0 t20,0 t20,0 t20,0 t20,0"/>
        <path class="wave-line faint" d="M342,247 q10,-6 20,0 t20,0 t20,0 t20,0 t20,0 t20,0 t20,0"/>
      </g>
      <polygon class="band" points="0,63 325,270 253,270 0,108"/>
      <polygon class="band-fold" points="175,262 253,270 175,270"/>
      <polygon class="band" points="498,63 498,108 245,270 173,270"/>
      <polygon class="band-fold" points="325,262 245,270 325,270"/>
      <text class="brand-name" x="250" y="117" text-anchor="middle">Vantilo</text>
      <text class="brand-web" x="250" y="136" text-anchor="middle">www.<tspan class="accent">vantilo</tspan>.com</text>
    </svg>
  </section>

  <section class="card card-back" aria-label="Card back">
    <svg viewBox="0 0 498 285" preserveAspectRatio="none">
      <defs>
        <linearGradient id="portraitTone" x1="0" y1="0" x2="0" y2="1">
          <stop offset="0" stop-color="var(--photo-light)"/>
          <stop offset="1" stop-color="var(--photo-dark)"/>
        </linearGradient>
      </defs>
      <rect class="bar" x="220" y="0" width="278" height="285"/>
      <g class="sea-waves">
        <path class="wave-line" d="M372,250 q10,-6 20,0 t20,0 t20,0 t20,0 t20,0 t20,0"/>
        <path class="wave-line faint" d="M382,262 q10,-6 20,0 t20,0 t20,0 t20,0 t20,0"/>
      </g>
      <polygon class="band" points="310,0 356,0 225,140 210,102"/>
      <polygon class="band-fold" points="210,102 225,140 210,150"/>
      <polygon class="band" points="210,150 232,128 355,285 312,285"/>

      <circle cx="107" cy="107" r="63" fill="var(--sky)"/>
      <circle cx="107" cy="107" r="60" fill="var(--paper)"/>
      <circle cx="107" cy="107" r="57" fill="url(#portraitTone)" role="img" aria-label="Portrait photo of Leon Marsh"/>

      <text class="person-name" x="107" y="214" text-anchor="middle">LEON MARSH</text>
      <text class="person-role" x="107" y="232" text-anchor="middle">FOUNDER &amp; CEO</text>

      <g class="contact-email">
        <circle class="icon-disc" cx="313" cy="99" r="16"/>
        <rect class="icon-line" x="305" y="94" width="16" height="11"/>
        <polyline class="icon-line" points="305,94 313,101 321,94"/>
        <text class="contact-text" x="337" y="103">l.marsh@vantilo.com</text>
      </g>
      <g class="contact-phone">
        <circle class="icon-disc" cx="313" cy="140" r="16"/>
        <path class="icon-fill" d="M306,133 l4,-2 l3,5 l-2,2 q2,4 6,6 l2,-2 l5,3 l-2,4 q-9,0 -16,-11 z"/>
        <text class="contact-text" x="337" y="135">+4455012378</text>
        <text class="contact-text" x="337" y="154">+4455012378</text>
      </g>
      <g class="contact-web">
        <circle class="icon-disc" cx="313" cy="182" r="16"/>
        <circle class="icon-line" cx="313" cy="182" r="8"/>
        <ellipse class="icon-line" cx="313" cy="182" rx="3.5" ry="8"/>
        <line class="icon-line" x1="305" y1="182" x2="321" y2="182"/>
        <text class="contact-text" x="335" y="186">www.vantilo.com</text>
      </g>
    </svg>
  </section>

</main>
</body>
</html>
```